Business Card of PebbleFinch
PebbleFinch
Bright & Fun-filled
Daniel Osei, CFA
President
412 Whitmore Suite 208
Irvine, CA 92655
daniel@pebblefinch.example
pebblefinch.example

```html
<!DOCTYPE html>
<html lang="en">
<head>
<meta charset="utf-8">
<title>PebbleFinch — Stationery Set</title>
<link href="https://fonts.googleapis.com/css2?family=Open+Sans:wght@400;600;700&display=swap" rel="stylesheet">
<style>
  :root{
    --frame-red:#e0262b;
    --stage:#e4e4e4;
    --paper:#ffffff;
    --brand-red:#e8262b;
    --brand-orange:#f7b21a;
    --orange-soft:rgba(247,178,26,.55);
    --orange-fade:rgba(247,178,26,0);
    --ink:#555555;
    --ink-soft:#8a8a8a;
    --folder-gray:#9d9d9d;
    --shadow:0 2px 5px rgba(0,0,0,.28);
  }
  *{box-sizing:border-box;margin:0;padding:0}
  html,body{width:1200px;height:974px;overflow:hidden}
  body{background:var(--frame-red);font-family:"Open Sans",Arial,sans-serif;color:var(--ink);position:relative}
  .stage{position:absolute;left:26px;top:26px;width:1148px;height:921px;background:var(--stage)}
  .piece{position:absolute;background:var(--paper);box-shadow:var(--shadow);overflow:hidden}
  .wave-band{position:absolute;left:0;width:100%;bottom:0;background:linear-gradient(to bottom,var(--orange-fade),var(--orange-soft) 60%,var(--orange-fade))}
  .wave-band.top{top:0;bottom:auto}
  .brand{display:flex;align-items:center;gap:3px;color:var(--brand-red);font-weight:700;letter-spacing:-.2px;position:absolute}
  .brand-mark{background:var(--brand-orange);display:block}
  .tiny{font-size:5px;line-height:1.45;color:var(--ink-soft)}

  .card-front{left:92px;top:84px;width:158px;height:87px}
  .card-front .brand{left:10px;top:14px;font-size:9px}
  .card-front .brand-mark{width:7px;height:7px}
  .card-front .contact{position:absolute;right:10px;top:12px;text-align:right}
  .card-front .contact strong{color:var(--ink);font-size:5.5px}
  .card-front .wave-band{height:26px}

  .card-back{left:92px;top:198px;width:158px;height:87px;display:flex;align-items:center;justify-content:center}
  .card-back .web{color:var(--brand-red);font-size:11px}
  .card-orange{left:92px;top:311px;width:158px;height:90px;background:var(--brand-orange);display:flex;align-items:center;justify-content:center}
  .card-orange .web{color:#fff;font-size:11px}

  .letterhead{left:276px;top:79px;width:250px;height:330px}
  .letterhead .brand{left:18px;top:30px;font-size:11px}
  .letterhead .brand-mark{width:9px;height:9px}
  .letterhead .address{position:absolute;right:16px;top:14px;text-align:right}
  .letterhead .wave-band{height:56px}

  .comp-card{left:558px;top:84px;width:74px;height:105px}
  .comp-card .brand{left:8px;top:8px;font-size:6px}
  .comp-card .brand-mark{width:5px;height:5px}
  .comp-card .contact{position:absolute;left:8px;top:44px}

  .env-small{left:558px;top:219px;width:166px;height:66px}
  .env-small .brand{left:10px;top:8px;font-size:7px}
  .env-small .brand-mark{width:5px;height:5px}
  .env-small .wave-band{height:28px}

  .env-dl{left:558px;top:311px;width:210px;height:90px}
  .env-dl .brand{left:10px;top:10px;font-size:8px}
  .env-dl .brand-mark{width:6px;height:6px}
  .env-dl .wave-band{height:30px}
  .env-dl .return{position:absolute;left:10px;top:60px}

  .env-stack{position:absolute;left:786px;top:200px;width:290px;height:210px}
  .envelope{position:absolute;width:256px;height:104px}
  .envelope svg{display:block;filter:drop-shadow(0 2px 3px rgba(0,0,0,.28))}
  .envelope.back{left:28px;top:0}
  .envelope.middle{left:14px;top:36px}
  .envelope.front{left:0;top:72px;height:130px}

  .folder{position:absolute;left:92px;top:448px;width:448px;height:382px}
  .folder-cover{position:absolute;left:0;top:0;width:448px;height:292px;background:var(--paper);box-shadow:var(--shadow);overflow:hidden}
  .folder-cover .wave-band.top{height:46px}
  .folder-cover .wave-band.lower{height:50px;bottom:44px}
  .folder-cover .brand{left:264px;top:40px;font-size:10px}
  .folder-cover .brand-mark{width:8px;height:8px}
  .folder-cover .center-brand{position:absolute;left:92px;top:130px}
  .folder-cover .center-brand .brand{position:static;font-size:8px}
  .folder-cover .center-brand .brand-mark{width:6px;height:6px}
  .folder-cover .center-brand .tiny{margin-top:4px}
  .pocket-left{position:absolute;left:0;top:248px;width:210px;height:134px;background:var(--brand-orange);box-shadow:var(--shadow)}
  .pocket-right{position:absolute;left:210px;top:248px;width:238px;height:134px;background:var(--folder-gray);box-shadow:var(--shadow)}
  .slot-card{position:absolute;left:288px;top:298px;width:118px;height:66px;background:var(--paper);box-shadow:var(--shadow);overflow:hidden}
  .slot-card .brand{left:8px;top:8px;font-size:6px}
  .slot-card .brand-mark{width:4px;height:4px}
  .slot-card .wave-band{height:22px}

  .cd{position:absolute;left:574px;top:508px;width:116px;height:116px;border-radius:50%;background:radial-gradient(circle,#fff 0 9px,#d8d8d8 9px 11px,#f4f4f4 11px 24px,#ffffff 24px 100%);box-shadow:var(--shadow)}
  .cd-sleeve{left:566px;top:644px;width:172px;height:184px}
  .cd-sleeve .brand{left:62px;top:40px;font-size:8px}
  .cd-sleeve .brand-mark{width:6px;height:6px}
  .cd-sleeve .wave-band{height:50px}

  .fax{left:769px;top:500px;width:258px;height:328px}
  .fax .brand{left:14px;top:18px;font-size:8px}
  .fax .brand-mark{width:6px;height:6px}
  .fax h1{position:absolute;left:14px;top:54px;font-size:17px;font-weight:600;color:var(--ink)}
  .fax-fields{position:absolute;left:14px;top:86px;width:228px;border-collapse:collapse}
  .fax-fields td{font-size:5px;color:var(--ink-soft);border-bottom:.7px solid #bbb;height:11px;vertical-align:bottom;width:50%}
  .fax-flags{position:absolute;left:14px;top:144px;display:flex;gap:8px;font-size:4.5px;color:var(--ink-soft)}
  .fax-flags span::before{content:"";display:inline-block;width:4px;height:4px;background:#666;margin-right:2px}
  .fax .wave-band{height:44px}
</style>
</head>
<body>
<main class="stage">

  <section class="piece card-front" aria-label="Business card front">
    <div class="brand"><span class="brand-mark"></span>PebbleFinch</div>
    <div class="contact tiny">
      <strong>Daniel Osei, CFA</strong><br>President<br>412 Whitmore Suite 208<br>Irvine, CA 92655<br>daniel@pebblefinch.example
    </div>
    <div class="wave-band" role="img" aria-label="Orange wave ornament"></div>
  </section>

  <section class="piece card-back"><span class="web">pebblefinch.example</span></section>
  <section class="piece card-orange"><span class="web">pebblefinch.example</span></section>

  <section class="piece letterhead" aria-label="Letterhead">
    <div class="address tiny">412 Whitmore Suite 208 · Irvine, CA 92655<br>daniel@pebblefinch.example · pebblefinch.example</div>
    <div class="brand"><span class="brand-mark"></span>PebbleFinch</div>
    <div class="wave-band" role="img" aria-label="Orange wave ornament"></div>
  </section>

  <section class="piece comp-card" aria-label="Compliment card">
    <div class="brand"><span class="brand-mark"></span>PebbleFinch</div>
    <div class="contact tiny">Daniel Osei, CFA<br>President<br>pebblefinch.example</div>
  </section>

  <section class="piece env-small" aria-label="Small envelope">
    <div class="brand"><span class="brand-mark"></span>PebbleFinch</div>
    <div class="wave-band" role="img" aria-label="Orange wave ornament"></div>
  </section>

  <section class="piece env-dl" aria-label="DL envelope">
    <div class="brand"><span class="brand-mark"></span>PebbleFinch</div>
    <div class="return tiny">412 Whitmore Suite 208<br>Irvine, CA 92655</div>
    <div class="wave-band" role="img" aria-label="Orange wave ornament"></div>
  </section>

  <div class="env-stack" aria-label="Envelope backs">
    <div class="envelope back">
      <svg width="256" height="104" viewBox="0 0 256 104"><rect x="0" y="12" width="256" height="92" fill="var(--paper)"/><polygon points="0,12 256,12 244,0 12,0" fill="var(--brand-orange)"/><polygon points="0,12 256,12 256,26 0,26" fill="var(--brand-orange)"/></svg>
    </div>
    <div class="envelope middle">
      <svg width="256" height="104" viewBox="0 0 256 104"><rect x="0" y="12" width="256" height="92" fill="var(--paper)"/><polygon points="0,12 256,12 244,0 12,0" fill="var(--brand-red)"/><polygon points="0,12 256,12 256,26 0,26" fill="var(--brand-red)"/></svg>
    </div>
    <div class="envelope front">
      <svg width="256" height="130" viewBox="0 0 256 130"><rect x="0" y="12" width="256" height="118" fill="var(--paper)"/><polygon points="0,12 256,12 244,0 12,0" fill="var(--brand-orange)"/><polygon points="0,12 256,12 256,26 0,26" fill="var(--brand-orange)"/></svg>
    </div>
  </div>

  <div class="folder" aria-label="Presentation folder">
    <div class="folder-cover">
      <div class="wave-band top" role="img" aria-label="Orange wave ornament"></div>
      <div class="brand"><span class="brand-mark"></span>PebbleFinch</div>
      <div class="center-brand">
        <div class="brand"><span class="brand-mark"></span>PebbleFinch</div>
        <div class="tiny">412 Whitmore Suite 208<br>Irvine, CA 92655<br>pebblefinch.example</div>
      </div>
      <div class="wave-band lower" role="img" aria-label="Orange wave ornament"></div>
    </div>
    <div class="pocket-left"></div>
    <div class="pocket-right"></div>
    <div class="slot-card">
      <div class="brand"><span class="brand-mark"></span>PebbleFinch</div>
      <div class="wave-band" role="img" aria-label="Orange wave ornament"></div>
    </div>
  </div>

  <div class="cd" aria-label="Disc"></div>

  <section class="piece cd-sleeve" aria-label="Disc sleeve">
    <div class="brand"><span class="brand-mark"></span>PebbleFinch</div>
    <div class="wave-band" role="img" aria-label="Orange wave ornament"></div>
  </section>

  <section class="piece fax" aria-label="Fax cover sheet">
    <div class="brand"><span class="brand-mark"></span>PebbleFinch</div>
    <h1>Fax</h1>
    <table class="fax-fields">
      <tr><td>To</td><td>From</td></tr>
      <tr><td>Fax</td><td>Pages</td></tr>
      <tr><td>Phone</td><td>Date</td></tr>
      <tr><td>Re</td><td>CC</td></tr>
    </table>
    <div class="fax-flags"><span>Urgent</span><span>For Review</span><span>Please Comment</span><span>Please Reply</span><span>Please Recycle</span></div>
    <div class="wave-band" role="img" aria-label="Orange wave ornament"></div>
  </section>

</main>
</body>
</html>
```